Website design and coding for new consultancy company

I need to have a full website designed for a new consultancy business I'm trying to establish. It's called Brightpath consult. I need an English version to begin with, and then there should be a Danish version as well, but I'll translate that myself. Just be aware that I need two language versions. The consultancy field that I'm targeting is Leadership - and specialist development. I offer to facilitate corporate academies for global companies as well as specific workshops within leadership- or team development, strategy sessions, personal coaching and facilitation of D&I (Diversity and inclusion) workshops. BTW my logo is not in high resolution - I need that as well.

Target Market(s)

Larger companies that has a need for developing their inhouse leadership capabilities or that wants to develop their specialists to take on more responsibility.

Industry/Entity Type

Consultancy business

Coding

Number of Pages Required

5+ page

Requirements
Must have
• Introduction site with a catch phrase. Book a meeting. Services that's beeing offered. Blog site with white papers etc. Language toggle (Danish/English). Cases/testimonials. About site. Contact site.

```html
<!DOCTYPE html>
<html lang="en">
<head>
<meta charset="utf-8">
<title>Brightpath Consult</title>
<link href="https://fonts.googleapis.com/css2?family=Raleway:wght@400;500;600;700;800&display=swap" rel="stylesheet">
<style>
:root{
  --blue:#1f6fc4;
  --blue-light:#2a86dc;
  --blue-deep:#175ea9;
  --ink:#161616;
  --text:#444;
  --white:#fff;
  --line:#dcdcdc;
}
*{box-sizing:border-box;margin:0;padding:0}
html,body{width:1200px;height:4373px;overflow:hidden}
body{font-family:"Raleway",sans-serif;color:var(--ink);background:var(--white)}
section,header,footer{position:relative;width:1200px;overflow:hidden}
.abs{position:absolute}
.heading{font-weight:700;font-size:31px;text-transform:uppercase;letter-spacing:.2px}
.heading .accent{color:var(--blue)}
.rule{position:absolute;height:4px;width:205px;background:var(--blue);clip-path:polygon(0 0,100% 35%,100% 65%,0 100%)}
.btn{position:absolute;display:flex;align-items:center;justify-content:center;background:var(--blue);color:var(--white);font-size:14px;font-weight:500}
.photo{position:absolute}

/* Header */
.site-header{height:98px;background:linear-gradient(90deg,var(--blue-deep),var(--blue-light));border-bottom:2px solid #0e3f75}
.brand{position:absolute;left:114px;top:24px;display:flex;align-items:center;gap:12px;color:var(--white)}
.brand-mark{width:14px;height:14px;background:var(--white)}
.brand-name{font-weight:800;font-size:34px;letter-spacing:1px}
.main-nav{position:absolute;left:448px;top:40px;display:flex;gap:30px;font-size:15px;color:var(--white);font-weight:500}
.main-nav .active{font-weight:700}
.lang{display:flex;align-items:center;gap:7px}
.lang-swatch{width:18px;height:12px;background:#d8d8e8}

/* Hero */
.hero{height:516px;background:var(--ink);color:var(--white)}
.hero h1{position:absolute;left:114px;top:118px;font-size:32px;line-height:44px;font-weight:700;text-transform:uppercase}
.hero p{position:absolute;left:114px;top:220px;font-size:18px;line-height:27px;width:440px;color:#e6e6e6}

/* About */
.about{height:608px}
.about p{position:absolute;left:597px;width:493px;font-size:14.5px;line-height:27px;color:var(--text)}
.about p .accent{color:var(--blue);font-weight:600}

/* Services */
.services{height:601px;background:linear-gradient(90deg,var(--blue-deep),var(--blue-light));color:var(--white)}
.service-card{position:absolute;top:208px;width:299px;height:296px;background:var(--white);color:var(--ink);text-align:center}
.service-icon{width:105px;height:105px;border:2px solid var(--blue);border-radius:50%;margin:32px auto 0;display:flex;align-items:center;justify-content:center}
.service-card h3{font-size:20px;font-weight:600;margin-top:18px}
.service-card p{font-size:13px;line-height:24px;color:#555;margin:14px 26px 0}
.arrow{position:absolute;width:30px;height:20px}

/* Approach */
.approach{height:624px}
.step{position:absolute;top:227px;width:298px;height:302px;border-bottom:5px solid var(--blue)}
.step-label{position:absolute;top:227px;height:48px;width:178px;left:60px;background:var(--white);display:flex;align-items:center;justify-content:center;font-size:17px;font-weight:500}
.step-label.is-active{background:var(--blue);color:var(--white)}

/* Contact */
.contact{height:701px;background:var(--ink);color:var(--white)}
.contact .intro{position:absolute;left:114px;top:174px;width:460px;font-size:15px;line-height:27px}
.field{position:absolute;background:var(--white);color:#555;font-size:13px;padding:0 16px;display:flex;align-items:center}
.field.message{align-items:flex-start;padding-top:16px}

/* Testimonials */
.testimonials{height:738px}
.quote-card{position:absolute;top:243px;height:385px;border:1px solid var(--line);text-align:center;padding:0 26px}
.quote-card.is-featured{background:linear-gradient(180deg,var(--blue-light),var(--blue));color:var(--white);border-color:transparent}
.avatar{width:102px;height:102px;border-radius:50%;margin:35px auto 0}
.quote-card blockquote{font-size:12.5px;line-height:22px;margin-top:28px;color:#555}
.quote-card.is-featured blockquote{color:#eef4fb}
.quote-card cite{display:block;font-style:normal;font-weight:600;font-size:15px;line-height:21px;margin-top:18px}

/* Footer */
.site-footer{height:438px;background:linear-gradient(90deg,var(--blue-deep),var(--blue-light));color:var(--white);text-align:center}
.footer-brand{position:absolute;left:0;right:0;top:88px;display:flex;justify-content:center;align-items:center;gap:14px}
.footer-brand .brand-name{font-size:44px}
.footer-brand .brand-mark{width:18px;height:18px}
.tagline{position:absolute;left:0;right:0;top:190px;font-size:18px;font-weight:500;letter-spacing:.3px}
.footer-nav{position:absolute;left:215px;top:248px;width:766px;height:58px;border:2px solid var(--white);display:flex;justify-content:center;align-items:center;gap:40px;font-size:15px;font-weight:500}
.socials{position:absolute;left:0;right:0;top:339px;display:flex;justify-content:center;gap:10px}
.social{width:34px;height:34px;border-radius:50%;background:var(--white);display:flex;align-items:center;justify-content:center}
.copyright{height:49px;background:var(--ink);color:#ddd;font-size:13px;display:flex;align-items:center;justify-content:center}
</style>
</head>
<body>

<header class="site-header">
  <div class="brand"><span class="brand-mark"></span><span class="brand-name">BRIGHTPATH</span></div>
  <nav class="main-nav">
    <span class="active">HOME</span><span>ABOUT</span><span>SERVICES</span><span>APPROACH</span><span>CLIENTS</span><span>CONTACT</span>
    <span class="lang"><span class="lang-swatch"></span>EN ⌄</span>
  </nav>
</header>

<section class="hero">
  <h1>Transforming potential<br>into performance.</h1>
  <p>Empowering leaders, strengthening teams, and driving organizational growth.</p>
  <div class="btn" style="left:114px;top:311px;width:198px;height:49px">Book a Consultation</div>
  <div class="photo" role="img" aria-label="Consultant presenting charts to a team in a meeting room" style="left:606px;top:84px;width:484px;height:348px;background:linear-gradient(135deg,#b9c7d6,#6f7f91 60%,#3b4653)"></div>
  <svg class="abs" style="left:606px;top:428px" width="484" height="22"><polygon points="0,4 484,6 484,20 0,8" fill="#1f6fc4"/></svg>
</section>

<section class="about">
  <div class="photo" role="img" aria-label="Portrait of the consultant in a navy blazer" style="left:114px;top:82px;width:410px;height:427px;background:linear-gradient(160deg,#f3f5f8,#cfd8e3 55%,#33425a)"></div>
  <svg class="abs" style="left:516px;top:90px" width="34" height="420"><polygon points="8,0 30,420 10,420" fill="#1f6fc4"/></svg>
  <h2 class="heading abs" style="left:597px;top:100px">About <span class="accent">Brightpath Consult</span></h2>
  <span class="rule" style="left:597px;top:156px"></span>
  <p style="top:190px">At <span class="accent">Brightpath Consult</span>, we believe that leadership is the cornerstone of organizational success. We partner with global companies to design and facilitate corporate academies, leadership programs, and specialist development initiatives that make a measurable difference.</p>
  <p style="top:312px">With experience in executive coaching, team development, strategy facilitation, and diversity &amp; inclusion workshops, we help organizations unlock potential, strengthen collaboration, and achieve lasting results.</p>
  <div class="btn" style="left:597px;top:455px;width:200px;height:49px">Read More About Me</div>
</section>

<section class="services">
  <h2 class="heading abs" style="left:114px;top:78px">Our Services</h2>
  <span class="rule" style="left:114px;top:135px;background:var(--white)"></span>
  <svg class="arrow" style="left:50px;top:346px" viewBox="0 0 30 20"><path d="M28 10H4M11 3 4 10l7 7" stroke="#fff" stroke-width="2.5" fill="none"/></svg>
  <svg class="arrow" style="left:1120px;top:346px" viewBox="0 0 30 20"><path d="M2 10h24M19 3l7 7-7 7" stroke="#fff" stroke-width="2.5" fill="none"/></svg>

  <article class="service-card" style="left:112px">
    <div class="service-icon"><svg width="56" height="56" viewBox="0 0 56 56" fill="none" stroke="#1f6fc4" stroke-width="2"><circle cx="28" cy="14" r="7"/><circle cx="14" cy="32" r="5"/><circle cx="42" cy="32" r="5"/><circle cx="28" cy="34" r="6"/><path d="M6 48c0-6 4-9 8-9s8 3 8 9M34 48c0-6 4-9 8-9s8 3 8 9M18 50c0-7 4-10 10-10s10 3 10 10"/></svg></div>
    <h3>Leadership Development</h3>
    <p>Custom corporate academies and leadership programs tailored to your business challenges and goals.</p>
  </article>
  <article class="service-card" style="left:451px">
    <div class="service-icon"><svg width="56" height="56" viewBox="0 0 56 56" fill="none" stroke="#1f6fc4" stroke-width="2"><circle cx="28" cy="12" r="5"/><circle cx="14" cy="22" r="5"/><circle cx="42" cy="22" r="5"/><path d="M20 34c0-6 4-9 8-9s8 3 8 9M6 36c0-5 4-7 8-7s8 2 8 7M34 36c0-5 4-7 8-7s8 2 8 7M4 46h48M10 46v6M46 46v6"/></svg></div>
    <h3>Team Development</h3>
    <p>Workshops that foster collaboration, trust, and high-performing teams across functions and cultures.</p>
  </article>
  <article class="service-card" style="left:791px">
    <div class="service-icon"><svg width="56" height="56" viewBox="0 0 56 56" fill="none" stroke="#1f6fc4" stroke-width="2"><rect x="6" y="12" width="36" height="28"/><path d="M13 34v-8M20 34v-12M27 34v-6"/><circle cx="38" cy="32" r="8"/><path d="M44 38l7 7"/></svg></div>
    <h3>Strategy Facilitation</h3>
    <p>Expert guidance to help leadership teams shape strategy, align priorities, and build a shared vision.</p>
  </article>
</section>

<section class="approach">
  <h2 class="heading abs" style="left:0;right:0;top:92px;text-align:center">Our <span class="accent">Approach</span></h2>
  <span class="rule" style="left:497px;top:153px"></span>
  <div class="step" role="img" aria-label="Two colleagues smiling while discussing work at a laptop" style="left:114px;background:linear-gradient(135deg,#6b8fb6,#a58f72 60%,#4e4638)"></div>
  <div class="step" role="img" aria-label="Man arranging sticky notes on a bright office wall" style="left:453px;background:linear-gradient(135deg,#f2f2f0,#d9d4cc 60%,#8f8374)"></div>
  <div class="step" role="img" aria-label="Woman presenting at a flip chart in a city office" style="left:791px;background:linear-gradient(135deg,#9aa6b2,#5e6670 55%,#2b2e33)"></div>
  <div class="step-label is-active" style="left:174px;top:2277px;top:454px">Understand</div>
  <div class="step-label" style="left:523px;top:454px;width:150px">Design</div>
  <div class="step-label" style="left:867px;top:458px;width:146px">Deliver</div>
</section>

<section class="contact">
  <h2 class="heading abs" style="left:114px;top:82px">Get in Touch</h2>
  <span class="rule" style="left:114px;top:137px"></span>
  <p class="intro">Let's talk about how we can strengthen leadership and performance in your organization.Fill out the form and we'll get</p>
  <div class="field" style="left:114px;top:260px;width:459px;height:47px">Full Name</div>
  <div class="field" style="left:114px;top:339px;width:204px;height:48px">Email Address</div>
  <div class="field" style="left:342px;top:339px;width:231px;height:48px">Company / Organization</div>
  <div class="field message" style="left:112px;top:418px;width:461px;height:110px">Message</div>
  <div class="btn" style="left:114px;top:558px;width:167px;height:48px;font-size:15px">Send Message</div>
  <svg class="abs" style="left:641px;top:88px" width="449" height="24"><polygon points="0,0 449,20 449,24 0,24" fill="#1f6fc4"/></svg>
  <div class="photo" role="img" aria-label="Four business professionals reviewing a tablet together" style="left:641px;top:108px;width:449px;height:500px;background:linear-gradient(135deg,#dfe3e6,#9ea6ad 45%,#5a5046 75%,#2f3b55)"></div>
</section>

<section class="testimonials">
  <h2 class="heading abs" style="left:0;right:0;top:108px;text-align:center">What our <span class="accent">Clients</span> Say</h2>
  <span class="rule" style="left:493px;top:165px"></span>
  <svg class="arrow" style="left:50px;top:428px" viewBox="0 0 30 20"><path d="M28 10H4M11 3 4 10l7 7" stroke="#222" stroke-width="2.5" fill="none"/></svg>
  <svg class="arrow" style="left:1120px;top:428px" viewBox="0 0 30 20"><path d="M2 10h24M19 3l7 7-7 7" stroke="#222" stroke-width="2.5" fill="none"/></svg>

  <article class="quote-card is-featured" style="left:114px;width:312px">
    <div class="avatar" role="img" aria-label="Client portrait" style="background:#f3c9c9;border:2px solid #fff"></div>
    <blockquote>"Brightpath Consult facilitated one of the most impactful leadership programs we've ever run. The sessions were engaging, practical, and tailored to our needs — our leaders came away with tools they could use immediately."</blockquote>
    <cite>— HR Director, Global<br>Manufacturing Company</cite>
  </article>
  <article class="quote-card" style="left:448px;width:311px">
    <div class="avatar" role="img" aria-label="Client portrait" style="background:#9cc6cf"></div>
    <blockquote>"The strategy workshop helped our leadership team align on priorities and create a clear roadmap. The facilitation style was both structured and inspiring."— Head of People &amp; Culture, Financial Services— Head of People &amp; Culture, Financial</blockquote>
    <cite>— Head of People &amp; Culture,<br>Financial Services</cite>
  </article>
  <article class="quote-card" style="left:781px;width:307px">
    <div class="avatar" role="img" aria-label="Client portrait" style="background:#a58ac4"></div>
    <blockquote>"The diversity &amp; inclusion workshop created real dialogue within our organization. It was not just theory — it changed how our teams work together""The diversity &amp; inclusion workshop created real dialogue within our organization. It was not just theory — it</blockquote>
    <cite>— Head of People &amp; Culture,<br>Financial Services</cite>
  </article>
</section>

<footer class="site-footer">
  <div class="footer-brand"><span class="brand-mark"></span><span class="brand-name">BRIGHTPATH</span></div>
  <p class="tagline">EMPOWERING LEADERS. STRENGTHENING TEAMS. DRIVING GROWTH.</p>
  <nav class="footer-nav"><span>HOME</span><span>ABOUT</span><span>SERVICES</span><span>OUR APPROACH</span><span>TESTIMONIALS</span><span>CONTACT</span></nav>
  <div class="socials">
    <span class="social" aria-label="Professional network"></span>
    <span class="social" aria-label="Phone"><svg width="18" height="18" viewBox="0 0 24 24"><path d="M6.6 10.8a15 15 0 0 0 6.6 6.6l2.2-2.2c.3-.3.7-.4 1-.2 1.1.4 2.3.6 3.6.6.6 0 1 .4 1 1V20c0 .6-.4 1-1 1A17 17 0 0 1 3 4c0-.6.4-1 1-1h3.5c.6 0 1 .4 1 1 0 1.3.2 2.5.6 3.6.1.3 0 .7-.2 1z" fill="#1f6fc4"/></svg></span>
    <span class="social" aria-label="Email"><svg width="18" height="18" viewBox="0 0 24 24" fill="none" stroke="#1f6fc4" stroke-width="2.2"><rect x="3" y="6" width="18" height="12" rx="1"/><path d="M3 7l9 6 9-6"/></svg></span>
  </div>
</footer>
<div class="copyright">Copyright © 2025 Brightpath Consult. All rights reserved.</div>

</body>
</html>
```